Crestline Gas and Plumbing Business Card Design

I am after a business card design for my plumbing business called 'Crestline Gas & Plumbing'. I do all types of plumbing and gas work and specialise in general maintenance plumbing. Would like to see designs using current logo

Industry/Entity Type

Plumbing

Contact Information for Business Card

Name - Dale Whitcombe
Phone number - 0455163027
Email - admin@crestlinegasandplumbing.example.com.au
ABN - 68204915336

```html
<!DOCTYPE html>
<html lang="en">
<head>
<meta charset="utf-8">
<title>Crestline Gas &amp; Plumbing – Business Card</title>
<link rel="stylesheet" href="https://fonts.googleapis.com/css2?family=Barlow:wght@400;500;600;700&display=swap">
<style>
  :root {
    --backdrop: #ebe9e8;
    --card-white: #ffffff;
    --brand-blue: #2e4a9e;
    --deep-blue: #353f96;
    --bright-blue: #2a5ea8;
    --flame-yellow: #f7c81a;
    --flame-orange: #f08a30;
    --text-grey: #555a63;
    --muted-grey: #8a8d93;
  }
  * { margin: 0; padding: 0; box-sizing: border-box; }
  html, body {
    width: 1200px; height: 1108px; overflow: hidden;
    background: var(--backdrop);
    font-family: "Barlow", sans-serif;
  }
  .canvas { position: relative; width: 1200px; height: 1108px; }

  .card {
    position: absolute;
    width: 560px; height: 320px;
    border-radius: 4px;
    overflow: hidden;
    box-shadow: 0 10px 28px rgba(0,0,0,0.12);
  }

  /* Front */
  .card-front { left: 80px; top: 150px; background: var(--card-white); }
  .flame-decoration {
    position: absolute; right: 0; top: 0;
    width: 110px; height: 220px;
    background: linear-gradient(160deg, var(--flame-yellow) 0%, var(--flame-orange) 100%);
    border-bottom-left-radius: 100% 90%;
  }
  .brand-name {
    position: absolute; left: 40px; top: 62px;
    display: flex; align-items: center; gap: 10px;
    font-weight: 700; font-size: 21px; letter-spacing: 0.4px;
    color: var(--brand-blue); text-transform: uppercase;
    white-space: nowrap;
  }
  .brand-dot {
    width: 22px; height: 22px; border-radius: 50%;
    background: var(--brand-blue);
  }
  .person { position: absolute; left: 40px; top: 140px; }
  .person-name { font-weight: 700; font-size: 24px; color: var(--brand-blue); }
  .person-role { font-size: 12px; color: var(--muted-grey); margin-top: 2px; }

  .contact-list {
    position: absolute; left: 40px; top: 210px;
    list-style: none;
    font-size: 13px; color: var(--text-grey);
  }
  .contact-list li { display: flex; align-items: center; gap: 10px; height: 22px; white-space: nowrap; }
  .contact-icon { width: 13px; height: 13px; flex: none; }

  /* Back */
  .card-back {
    left: 560px; top: 600px;
    background: radial-gradient(circle at 55% 40%, var(--bright-blue) 0%, var(--deep-blue) 75%);
    color: #fff;
    display: flex; flex-direction: column; align-items: center; justify-content: center;
    text-align: center;
  }
  .back-brand {
    display: flex; align-items: center; gap: 12px;
    font-weight: 700; font-size: 26px; letter-spacing: 0.5px; text-transform: uppercase;
    white-space: nowrap;
  }
  .back-dot { width: 28px; height: 28px; border-radius: 50%; background: #fff; }
  .tagline {
    margin-top: 34px;
    font-weight: 600; font-size: 14px; letter-spacing: 0.6px; line-height: 1.45;
    text-transform: uppercase;
  }
</style>
</head>
<body>
<main class="canvas">

  <section class="card card-front">
    <div class="flame-decoration" role="img" aria-label="Yellow to orange flame swoosh decoration"></div>

    <div class="brand-name"><span class="brand-dot"></span>Crestline Gas &amp; Plumbing</div>

    <div class="person">
      <p class="person-name">Dale Whitcombe</p>
      <p class="person-role">Director</p>
    </div>

    <ul class="contact-list">
      <li>
        <svg class="contact-icon" viewBox="0 0 24 24"><path d="M12 2a7 7 0 0 0-7 7c0 5 7 13 7 13s7-8 7-13a7 7 0 0 0-7-7zm0 9.5A2.5 2.5 0 1 1 12 6.5a2.5 2.5 0 0 1 0 5z" fill="var(--flame-orange)"/></svg>
        418 Harlan Ave Suite 3, Fresno CA 93711
      </li>
      <li>
        <svg class="contact-icon" viewBox="0 0 24 24"><path d="M6.6 10.8a15 15 0 0 0 6.6 6.6l2.2-2.2a1 1 0 0 1 1-.25 11.4 11.4 0 0 0 3.6.57 1 1 0 0 1 1 1V20a1 1 0 0 1-1 1A17 17 0 0 1 3 4a1 1 0 0 1 1-1h3.5a1 1 0 0 1 1 1c0 1.25.2 2.45.57 3.57a1 1 0 0 1-.25 1z" fill="var(--flame-orange)"/></svg>
        0455163027
      </li>
      <li>
        <svg class="contact-icon" viewBox="0 0 24 24"><rect x="2" y="5" width="20" height="14" rx="2" fill="var(--flame-orange)"/><path d="M3 6l9 7 9-7" stroke="#fff" stroke-width="1.8" fill="none"/></svg>
        admin@crestlinegasandplumbing.example.com.au
      </li>
      <li>
        <svg class="contact-icon" viewBox="0 0 24 24"><circle cx="12" cy="12" r="9" fill="none" stroke="var(--flame-orange)" stroke-width="2"/><path d="M3 12h18M12 3c3 3 3 15 0 18M12 3c-3 3-3 15 0 18" fill="none" stroke="var(--flame-orange)" stroke-width="1.6"/></svg>
        www.crestlinegasandplumbing.example.com.au
      </li>
    </ul>
  </section>

  <section class="card card-back">
    <div class="back-brand"><span class="back-dot"></span>Crestline Gas &amp; Plumbing</div>
    <p class="tagline">All types of plumbing and gas work<br>and specialise in general maintenance plumbing</p>
  </section>

</main>
</body>
</html>
```